Tru Wave and Link post card design

We need a postcard to hand out to prospective clients detailing what we do with contact details kept to just a mobile phone number.
Tru Wave and Link is a communications networking company specialising in computer cabling, phone cabling, fibre optics, CCTV, particularly for small business. We offer licenced technicians with over 20 years experience in this field. We service greater Brisbane. Designs that incorporate colours from our logo would be great and that is similar to our business card.
Communications

```html
<!DOCTYPE html>
<html lang="en">
<head>
<meta charset="utf-8">
<title>Tru Wave and Link – Postcard</title>
<link rel="stylesheet" href="https://fonts.googleapis.com/css2?family=Arimo:wght@400;700&display=swap">
<style>
  :root {
    --frame-green: #52f20c;
    --brand-green: #5ce61a;
    --pale-green: #ccff66;
    --service-yellow: #d8f27a;
    --ink: #000000;
    --paper: #ffffff;
    --ghost: #2a2a2a;
    --divider: #6a6a6a;
  }
  * { margin: 0; padding: 0; box-sizing: border-box; }
  html, body { width: 780px; height: 1200px; overflow: hidden; background: var(--paper); }
  body { font-family: "Arimo", Arial, sans-serif; position: relative; }

  .card { position: absolute; left: 0; width: 780px; height: 600px; background: var(--frame-green); }
  .card--front { top: 0; }
  .card--back { top: 600px; border-top: 1px solid var(--divider); }

  .front-panel { position: absolute; left: 30px; top: 30px; width: 720px; height: 540px; background: var(--ink); overflow: hidden; }
  .fibre-visual {
    position: absolute; right: 0; top: 0; width: 360px; height: 240px;
    background: radial-gradient(ellipse at 85% 35%, #b8ff4a 0%, #5fc20f 22%, #1f4a05 50%, rgba(0,0,0,0) 75%);
  }
  .brand { position: absolute; display: flex; align-items: center; gap: 12px; }
  .brand__mark { width: 44px; height: 44px; border-radius: 50%; background: var(--brand-green); flex: none; }
  .brand__name { color: var(--brand-green); font-weight: 700; font-size: 34px; white-space: nowrap; }
  .front-panel .brand { left: 24px; top: 52px; }

  .contact { position: absolute; color: var(--paper); }
  .contact__name { font-weight: 700; font-size: 24px; white-space: nowrap; }
  .contact__line { font-size: 21px; white-space: nowrap; }
  .front-panel .contact { left: 21px; top: 168px; }
  .front-panel .contact__name { margin-bottom: 10px; }
  .front-panel .contact__line { margin-bottom: 8px; }

  .service { position: absolute; color: var(--service-yellow); font-size: 20px; white-space: nowrap; }
  .ghost-line {
    position: absolute; left: -40px; top: 446px; font-size: 33px; color: var(--ghost); white-space: nowrap;
  }
  .tagline { position: absolute; left: 0; width: 720px; top: 486px; text-align: center; color: var(--paper); font-size: 26px; white-space: nowrap; }

  .back-panel { position: absolute; left: 30px; top: 28px; width: 720px; height: 542px; background: var(--paper); overflow: hidden; }
  .service-bands { position: absolute; left: 0; top: 0; }
  .band-label { position: absolute; color: var(--ink); font-size: 23px; white-space: nowrap; }
  .band-list { position: absolute; left: 10px; top: 339px; list-style: none; font-size: 23px; }
  .band-list li { display: flex; align-items: center; gap: 12px; height: 35px; }
  .band-list svg { width: 13px; height: 13px; }

  .back-panel .brand { right: 14px; top: 42px; }
  .back-panel .brand__name { font-size: 32px; }
  .back-panel .contact { right: 12px; top: 140px; color: var(--ink); text-align: right; }
  .back-panel .contact__name { font-size: 22px; margin-bottom: 8px; }
  .back-panel .contact__line { font-size: 22px; margin-bottom: 4px; }
  .write-lines { position: absolute; left: 0; top: 0; }
</style>
</head>
<body>

<section class="card card--front">
  <div class="front-panel">
    <div class="fibre-visual" role="img" aria-label="Photograph of glowing green fibre optic strands fanning out"></div>

    <div class="brand">
      <span class="brand__mark"></span>
      <span class="brand__name">Tru Wave and Link</span>
    </div>

    <div class="contact">
      <p class="contact__name">Daniel Reeve</p>
      <p class="contact__line">Mob: 0412 305 918</p>
      <p class="contact__line">Servicing greater Brisbane</p>
    </div>

    <p class="service" style="left:130px; top:300px;">COMPUTER CABLING</p>
    <p class="service" style="left:260px; top:334px;">PHONE CABLING</p>
    <p class="service" style="left:382px; top:368px;">FIBRE OPTICS</p>
    <p class="service" style="left:328px; top:393px;">Cabling / Testing / Cleaning</p>
    <p class="service" style="left:560px; top:422px;">CCTV</p>

    <p class="ghost-line" aria-hidden="true">Licensed technicians with over 20 years experience</p>
    <p class="tagline">Licensed technicians with over 20 years experience</p>
  </div>
</section>

<section class="card card--back">
  <div class="back-panel">
    <svg class="service-bands" width="720" height="542" viewBox="0 0 720 542" aria-hidden="true">
      <polygon points="0,0 415,0 110,542 0,542" fill="var(--ink)"/>
      <polygon points="0,35 375,35 323,134 0,134" fill="var(--pale-green)"/>
      <polygon points="0,161 305,161 253,259 0,259" fill="var(--pale-green)"/>
      <polygon points="0,284 234,284 110,505 0,505" fill="var(--pale-green)"/>
    </svg>

    <p class="band-label" style="left:38px; top:68px;">COMPUTER CABLING</p>
    <p class="band-label" style="left:30px; top:196px;">PHONE CABLING</p>
    <p class="band-label" style="left:10px; top:303px;">FIBRE OPTICS</p>
    <ul class="band-list">
      <li><svg viewBox="0 0 13 13"><polygon points="0,3 13,0 10,13 0,13" fill="var(--brand-green)"/></svg>Cabling</li>
      <li><svg viewBox="0 0 13 13"><polygon points="0,3 13,0 10,13 0,13" fill="var(--brand-green)"/></svg>Testing</li>
      <li><svg viewBox="0 0 13 13"><polygon points="0,3 13,0 10,13 0,13" fill="var(--brand-green)"/></svg>Cleaning</li>
    </ul>
    <p class="band-label" style="left:10px; top:458px;">CCTV</p>

    <div class="brand">
      <span class="brand__mark"></span>
      <span class="brand__name">Tru Wave and Link</span>
    </div>

    <div class="contact">
      <p class="contact__name">Daniel Reeve</p>
      <p class="contact__line">Mob: 0412 305 918</p>
      <p class="contact__line">Servicing greater Brisbane</p>
    </div>

    <svg class="write-lines" width="720" height="542" viewBox="0 0 720 542" aria-hidden="true">
      <line x1="330" y1="324" x2="713" y2="324" stroke="var(--ink)" stroke-width="3"/>
      <line x1="283" y1="389" x2="713" y2="389" stroke="var(--ink)" stroke-width="3"/>
      <line x1="231" y1="454" x2="713" y2="454" stroke="var(--ink)" stroke-width="3"/>
    </svg>
  </div>
</section>

</body>
</html>
```